Small Business Consulting Firm Needs Business Card Design

Need a sleek modern business card with 2 sides matching the colors of our logo. We will be placing these with a mailer we are sending out. These business cards will only ever be given to business owners. We operate helping businesses who are struggling with cash flow or finances. If the green and blue design needs to be moved to the right of "Harborline Crest Consulting" for aesthetic purposes that is ok. We will need an editable file if possible. We would like to include the reps name, email, website, and phone number. For now just use Peter Vance, pvance@harborlinecrest.com, www.harborlinecrest.com, and 833-555-0172.

```html
<!DOCTYPE html>
<html lang="en">
<head>
<meta charset="utf-8">
<title>Harborline Crest Consulting – Business Card</title>
<link rel="stylesheet" href="https://fonts.googleapis.com/css2?family=Lato:wght@300;400;700&display=swap">
<style>
  :root {
    --bg: #a3a3a3;
    --card: #ffffff;
    --brand-blue: #0a7cc4;
    --brand-green: #7cbd3c;
    --name-blue: #1f6fb5;
    --ink: #2f2f2f;
  }
  * { margin: 0; padding: 0; box-sizing: border-box; }
  html, body { width: 1200px; height: 750px; overflow: hidden; }
  body {
    background: var(--bg);
    font-family: "Lato", sans-serif;
    position: relative;
  }
  .card {
    position: absolute;
    top: 221px;
    width: 540px;
    height: 308px;
    background: var(--card);
    border-radius: 16px;
    overflow: hidden;
  }
  .card--front { left: 54px; }
  .card--back { left: 606px; }
  .card__accent {
    position: absolute;
    top: 0;
    bottom: 0;
    width: 42px;
    background: linear-gradient(180deg, var(--brand-blue), var(--brand-green));
  }
  .card--front .card__accent { left: 0; }
  .card--back .card__accent {
    right: 0;
    background: linear-gradient(0deg, var(--brand-blue), var(--brand-green));
  }
  .brand {
    position: absolute;
    left: 0;
    right: 0;
    text-align: center;
    color: var(--ink);
    font-weight: 300;
  }
  .brand__mark {
    display: block;
    margin: 0 auto 12px;
    background: var(--brand-green);
  }
  .brand__name {
    display: block;
    letter-spacing: 0.06em;
    text-transform: uppercase;
    white-space: nowrap;
  }
  .brand__tag {
    display: block;
    text-transform: uppercase;
    letter-spacing: 0.35em;
  }
  .card--front .brand { top: 30px; left: 42px; }
  .card--front .brand__mark { width: 38px; height: 38px; }
  .card--front .brand__name { font-size: 18px; }
  .card--front .brand__tag { font-size: 9px; margin-top: 1px; }
  .card--back .brand { top: 96px; right: 42px; }
  .card--back .brand__mark { width: 44px; height: 44px; }
  .card--back .brand__name { font-size: 21px; }
  .card--back .brand__tag { font-size: 10.5px; margin-top: 2px; }

  .rep {
    position: absolute;
    top: 152px;
    left: 42px;
    right: 0;
    text-align: center;
  }
  .rep__name {
    color: var(--name-blue);
    font-weight: 700;
    font-size: 20px;
    line-height: 1.1;
  }
  .rep__role {
    color: var(--brand-green);
    font-size: 13px;
    margin-top: 2px;
  }
  .contact-icons {
    display: flex;
    justify-content: center;
    gap: 13px;
    margin-top: 14px;
  }
  .contact-icons svg { width: 16px; height: 16px; }
  .contact-list {
    list-style: none;
    margin-top: 7px;
    color: var(--ink);
    font-size: 14.5px;
    line-height: 19px;
  }
</style>
</head>
<body>
  <section class="card card--front">
    <div class="card__accent" role="img" aria-label="Blue and green brand accent along the card edge"></div>
    <div class="brand">
      <span class="brand__mark"></span>
      <span class="brand__name">Harborline Crest</span>
      <span class="brand__tag">Consulting</span>
    </div>
    <div class="rep">
      <p class="rep__name">Peter Vance</p>
      <p class="rep__role">Representative</p>
      <div class="contact-icons" aria-hidden="true">
        <svg viewBox="0 0 16 16" fill="none" stroke="var(--brand-green)" stroke-width="1.4">
          <path d="M2,6 C4,3 12,3 14,6 L12.5,7.5 L10.5,6.5 V5.5 H5.5 V6.5 L3.5,7.5 Z" fill="var(--brand-green)"/>
          <path d="M4.5,8 H11.5 L13,13 H3 Z" fill="var(--brand-green)"/>
        </svg>
        <svg viewBox="0 0 16 16" fill="none" stroke="var(--brand-green)" stroke-width="1.3">
          <path d="M2,6 L8,2 L14,6 V14 H2 Z"/>
          <path d="M2,6 L8,10 L14,6"/>
        </svg>
        <svg viewBox="0 0 16 16" fill="none" stroke="var(--brand-green)" stroke-width="1.2">
          <circle cx="8" cy="8" r="6.3"/>
          <ellipse cx="8" cy="8" rx="2.8" ry="6.3"/>
          <path d="M1.7,8 H14.3 M2.8,4.8 H13.2 M2.8,11.2 H13.2"/>
        </svg>
      </div>
      <ul class="contact-list">
        <li>833-555-0172</li>
        <li>pvance@harborlinecrest.com</li>
        <li>www.harborlinecrest.com</li>
      </ul>
    </div>
  </section>

  <section class="card card--back">
    <div class="card__accent" role="img" aria-label="Blue and green brand accent along the card edge"></div>
    <div class="brand">
      <span class="brand__mark"></span>
      <span class="brand__name">Harborline Crest</span>
      <span class="brand__tag">Consulting</span>
    </div>
  </section>
</body>
</html>
```